R.Morvane LLC Organizational Change and Development

I am starting my own company as a a senior facilitator, keynote speaker, executive coach, webinar training instructor, quality management adviser, and classroom presenter. I have taught diversity and cultural competence, organizational development, change management, leadership, organizational dynamics, team-building, accountability, negotiation, work-life balance, quality management, TRAK, and hundreds of web based trainings. I have a PhD. in Counseling Psychology, MBA, B.S. in Human Development, Family Studies, and a Master’s Practitioner of Neurolinguistic Programming. My degrees and certifications give me a foundation for advising a wide variety of people, industries, and cultures at all organizational levels. I would like a design that's fun, engaging, humorous, progressive, and has a professional feel. I really like the colors burgundy wine.

Target Market(s)

corporate America

Industry/Entity Type

Training

Number of Pages Required

5+ page

Colors
eb1f26
f04a50
3176b4
33a6d7

Requirements
Must have
• my different areas of expertise - fun visuals -easy for me to use
Should not have
• something that looks stiff, too traditional or boring

```html
<!DOCTYPE html>
<html lang="en">
<head>
<meta charset="utf-8">
<title>R. Morvane LLC – Organizational Change and Development</title>
<link href="https://fonts.googleapis.com/css2?family=Lora:ital,wght@1,600;1,700&family=Montserrat:wght@400;600;700&display=swap" rel="stylesheet">
<style>
:root{
  --burgundy:#8b2e36;
  --burgundy-dark:#6e1f27;
  --red:#eb1f26;
  --coral:#f04a50;
  --blue:#3176b4;
  --navy:#1d4f9a;
  --sky:#33a6d7;
  --ink:#333;
  --muted:#666;
  --brown-1:#5b3a2b;
  --brown-2:#3a2419;
  --teal:#b4dcdc;
  --teal-dark:#8cc4c5;
  --orange:#f59a2b;
  --footer:#7a7a7a;
}
*{box-sizing:border-box;margin:0;padding:0}
html,body{width:1045px;height:1200px;overflow:hidden;background:#fff}
body{position:relative;font-family:"Montserrat",sans-serif;color:var(--ink)}
.abs{position:absolute}
a{color:inherit;text-decoration:none}

/* header */
.brand{left:106px;top:14px;font-family:"Montserrat",sans-serif;font-weight:700;font-size:40px;line-height:46px;color:var(--burgundy);letter-spacing:1px;white-space:nowrap}
.contact{left:570px;top:5px;font-family:"Lora",serif;font-style:italic;font-weight:600;color:var(--navy);font-size:9.5px;line-height:16px}
.roles{left:568px;top:40px;font-family:"Lora",serif;font-style:italic;font-weight:700;font-size:11.5px;color:var(--red);word-spacing:1px}
.roles span.sep{margin:0 10px}

/* nav */
.nav{left:0;top:83px;width:1045px;height:25px;background:var(--burgundy)}
.nav ul{list-style:none;display:flex;position:absolute;left:102px;top:0;height:25px}
.nav li{font-size:8.5px;font-weight:700;color:#fff;line-height:25px;padding:0 13px}
.nav li.active{background:var(--burgundy-dark);padding:0 15px}
.social{right:115px;top:7px;display:flex;gap:7px}
.social span{width:20px;height:12px;font-size:6px;font-weight:700;color:#fff;text-align:center;line-height:12px}
.social .s1{background:#3b5b98}.social .s2{background:var(--sky)}.social .s3{background:#1c6ea8}

/* hero */
.hero{left:0;top:108px;width:1045px;height:231px;background:radial-gradient(ellipse at 40% 40%,var(--brown-1),var(--brown-2))}
.hero h1{position:absolute;left:115px;top:34px;color:#fff;font-size:14.5px;font-weight:700;line-height:23px;letter-spacing:.4px}
.hero blockquote{position:absolute;left:116px;top:88px;color:#f1e7e2;font-size:9px;line-height:16.5px;width:420px}
.hero cite{display:block;font-style:normal;font-weight:700;font-size:8.5px}
.btn-line{position:absolute;top:174px;height:19px;width:94px;border:1px solid #cbb9ae;color:#eee;font-size:8.5px;text-align:center;line-height:17px;border-radius:2px}
.portrait{left:670px;top:112px;width:250px;height:205px;border-radius:120px 120px 10px 10px;background:radial-gradient(ellipse at 55% 30%,#f1d9a6 0%,#d8b57f 35%,#2a2522 70%,rgba(42,37,34,0) 100%)}

/* intro */
.intro{left:113px;top:350px;width:392px}
.intro h2{font-family:"Montserrat",sans-serif;font-weight:700;color:var(--navy);font-size:14px;letter-spacing:1px}
.intro p{font-size:8.6px;line-height:16.6px;color:var(--muted);text-align:justify;margin-top:2px}
.more{font-size:8px;color:var(--blue)}
.more::before{content:"▸";margin-right:10px;font-size:6px}
.video{left:527px;top:318px;width:465px;height:155px;background:#fff;box-shadow:0 3px 6px rgba(0,0,0,.25)}
.video-screen{position:absolute;left:6px;top:6px;width:451px;height:144px;background:linear-gradient(100deg,#0b1b5a,#1553b8 55%,#0a1d5c)}

/* feature cards */
.cards{left:118px;top:510px;width:820px;height:108px;background:repeating-linear-gradient(90deg,#f6f6f6 0 2px,#fff 2px 4px)}
.card{top:523px;width:245px;text-align:center}
.card-img{width:243px;height:89px;border:1px solid #ccc}
.card h3{font-size:12px;font-weight:400;margin-top:8px;color:#222}
.card p{font-size:7.1px;line-height:14px;color:#555;margin-top:4px}
.card .more{display:block;margin-top:7px}

/* lower */
.section-title{font-size:12px;font-weight:400;color:#222}
.testimonials{left:108px;top:777px;width:223px}
.quote{position:relative;padding-left:27px;border-bottom:1px dotted #bbb;padding-bottom:6px;margin-top:8px}
.quote::before{content:"\201C\201C";position:absolute;left:0;top:-6px;font-family:Georgia,serif;font-size:26px;color:#aaa;letter-spacing:-6px}
.quote p{font-size:7.4px;line-height:12.7px;color:#555;text-align:justify}
.quote b{font-size:7.5px;color:var(--navy)}
.blog{left:378px;top:777px;width:270px}
.post{display:flex;gap:9px;border-bottom:1px dotted #bbb;padding:8px 0 6px}
.post-img{width:100px;height:42px;flex:none}
.post h4{font-size:7.6px;color:var(--blue);line-height:10px;font-weight:700}
.post .meta{font-size:7px;color:#555;margin-top:3px;display:flex;gap:16px}
.post .meta a{color:var(--orange);font-weight:600}
.signup{left:693px;top:778px;width:282px;height:200px;background:var(--teal)}
.signup-head{height:24px;background:var(--teal-dark);color:#fff;font-size:12.5px;font-weight:700;text-align:center;line-height:24px;letter-spacing:.5px}
.signup h5{position:absolute;top:126px;width:100%;text-align:center;font-size:13px;font-weight:600;line-height:13px;color:#222}
.signup-bar{position:absolute;left:0;top:161px;width:282px;height:39px;background:#a3d3d4}
.field{position:absolute;background:#fff;border:1px solid #ccc;font-size:7px;color:#777;padding-left:6px}
.btn-orange{position:absolute;background:var(--orange);color:#fff;font-size:7.5px;font-weight:700;text-align:center;border-radius:3px}

.seen{left:0;top:1030px;width:1045px;text-align:center;font-size:10px;color:#444}
.press{top:1064px;font-weight:700;color:var(--navy);font-size:13px;white-space:nowrap}

/* footer */
.footer{left:0;top:1127px;width:1045px;height:73px;background:var(--footer);color:#fff}
.foot-nav{position:absolute;left:112px;top:19px;font-size:7.5px}
.foot-nav span.sep{margin:0 8px}
.foot-rule{position:absolute;left:112px;top:33px;width:480px;border-top:1px solid #999}
.foot-legal{position:absolute;left:120px;top:40px;font-size:7.5px}
.news-title{position:absolute;left:789px;top:11px;font-size:7.5px;letter-spacing:.3px}
</style>
</head>
<body>

<header>
  <div class="abs brand">R. MORVANE</div>
  <div class="abs contact">Renata Morvane PhD, MBA<br>(555) 014-2290</div>
  <div class="abs roles">Senior Facilitator<span class="sep">|</span>Keynote Speaker<span class="sep">|</span>Executive coach</div>
</header>

<nav class="abs nav">
  <ul>
    <li class="active">HOME</li><li>SPEAKING</li><li>CONSULTING</li><li>TRAINING</li><li>BOOKS</li><li>RESOURCES</li><li>ABOUT</li><li>CONTACT</li><li>TESTIMONIALS</li>
  </ul>
  <div class="abs social"><span class="s1">Hub</span><span class="s2">Buzz</span><span class="s3">Pro</span></div>
</nav>

<section class="abs hero">
  <h1>Award Winning Technology Consultant, Entrepreneur,<br>Small Business Leader, and Motivational Speaker</h1>
  <blockquote>"Morvane is a remarkable executive and an incredibly sensitive business woman, who is a wonderful presenter of information and ideas..."<cite>- Arlen, Author &amp; Speaker</cite></blockquote>
  <a class="btn-line" style="left:122px">Learn More</a>
  <a class="btn-line" style="left:238px">Watch Videos</a>
</section>
<div class="abs portrait" role="img" aria-label="Portrait photo of the speaker in a dark blazer"></div>

<section class="abs intro">
  <h2>R.MORVANE</h2>
  <p>I am starting my own company as a a senior facilitator, keynote speaker, executive coach, webinar training instructor, quality management adviser, and classroom presenter. I have taught diversity and cultural competence, organizational development, change management, leadership, organizational dynamics, team-</p>
  <a class="more">Read More About Morvane</a>
</section>

<div class="abs video">
  <div class="video-screen" role="img" aria-label="Video still of the speaker presenting on a large stage screen"></div>
  <svg class="abs" style="left:0;top:0" width="465" height="155" aria-hidden="true">
    <ellipse cx="263" cy="80" rx="72" ry="46" fill="#fff" fill-opacity=".85"/>
    <polygon points="255,62 255,98 282,80" fill="#14244d"/>
  </svg>
</div>

<div class="abs cards"></div>
<article class="abs card" style="left:144px">
  <div class="card-img" role="img" aria-label="Photo of an open book on a stack of books" style="background:linear-gradient(180deg,#6b3a1f,#c8914f 60%,#f3e4c4)"></div>
  <h3>Books</h3>
  <p>I am starting my own company as a a senior facilitator,<br>keynote speaker, executive coach, webinar training instructor,<br>quality management adviser, and classroom presenter. I have<br>taught diversity and cultural competence, organizational<br>development, change management, leadership, organiza-</p>
  <a class="more">Read More</a>
</article>
<article class="abs card" style="left:410px">
  <div class="card-img" role="img" aria-label="Photo of a microphone in front of an audience" style="background:radial-gradient(circle at 50% 55%,#d8c6a0,#9a5a2a 40%,#5a2a12)"></div>
  <h3>Speaking</h3>
  <p>I am starting my own company as a a senior facilitator,<br>keynote speaker, executive coach, webinar training instructor,<br>quality management adviser, and classroom presenter. I have<br>taught diversity and cultural competence, organizational<br>development, change management, leadership, organiza-</p>
  <a class="more">Read More</a>
</article>
<article class="abs card" style="left:676px">
  <div class="card-img" role="img" aria-label="Photo of a pen over a calendar page" style="background:linear-gradient(160deg,#bfc3c8,#f2f2f2 50%,#d9dadd)"></div>
  <h3>Upcoming Events</h3>
  <p>I am starting my own company as a a senior facilitator,<br>keynote speaker, executive coach, webinar training instructor,<br>quality management adviser, and classroom presenter. I have<br>taught diversity and cultural competence, organizational<br>development, change management, leadership, organiza-</p>
  <a class="more">Read More</a>
</article>

<section class="abs testimonials">
  <h2 class="section-title">Testimonials</h2>
  <div class="quote"><p>I am starting my own company as a senior facilitator, keynote speaker, executive coach, webinar training instructor, quality management</p><b>- Dunmore</b></div>
  <div class="quote"><p>I am starting my own company as a senior facilitator, keynote speaker, executive coach, webinar training instructor, quality management</p><b>- Dunmore</b></div>
  <div class="quote"><p>I am starting my own company as a senior facilitator, keynote speaker, executive coach, webinar training instructor, quality management</p><b>- Dunmore</b></div>
</section>

<section class="abs blog">
  <h2 class="section-title"><svg width="24" height="15" viewBox="0 0 24 15" style="vertical-align:-2px;margin-right:4px" aria-hidden="true"><rect x="0" y="1" width="15" height="9" rx="2" fill="var(--orange)"/><polygon points="3,10 7,10 3,14" fill="var(--orange)"/><rect x="9" y="4" width="15" height="9" rx="2" fill="#f7b35a"/></svg>Latest from Blog</h2>
  <div class="post"><div class="post-img" role="img" aria-label="Photo of a conference hall" style="background:linear-gradient(180deg,#2a2f5a,#a4322e)"></div><div><h4>Being a writer means dreaming with your eyes open and sharing what you see.</h4><div class="meta">November 14 2014<a>▸ Read More</a></div></div></div>
  <div class="post"><div class="post-img" role="img" aria-label="Photo of a workshop group" style="background:linear-gradient(90deg,#d9b27a,#eef1f4)"></div><div><h4>Being a writer means dreaming with your eyes open and sharing what you see.</h4><div class="meta">November 14 2014<a>▸ Read More</a></div></div></div>
  <div class="post"><div class="post-img" role="img" aria-label="Photo of hands writing on paper" style="background:linear-gradient(135deg,#f3e6df,#d9a89a)"></div><div><h4>Being a writer means dreaming with your eyes open and sharing what you see.</h4><div class="meta">November 14 2014<a>▸ Read More</a></div></div></div>
</section>

<aside class="abs signup">
  <div class="signup-head">Sign up for Email Updates</div>
  <div class="abs" role="img" aria-label="Cover images of three free business books" style="left:30px;top:40px;width:225px;height:80px;background:linear-gradient(90deg,#e8eef0 0 35%,#d6322f 35% 65%,#3a3a3a 65%)"></div>
  <h5>Get Free Books &amp;<br>Exclusive Updates</h5>
  <div class="signup-bar">
    <div class="field" style="left:13px;top:12px;width:203px;height:17px;line-height:15px">Email Address</div>
    <div class="btn-orange" style="left:223px;top:12px;width:54px;height:17px;line-height:17px">GET A COPY</div>
  </div>
</aside>

<div class="abs seen">As Seen On</div>
<div class="abs press" style="left:178px">Harbor City Ledger</div>
<div class="abs press" style="left:412px">Bayline Monthly</div>
<div class="abs press" style="left:548px">Coast Tribune</div>
<div class="abs press" style="left:672px">SBX</div>
<div class="abs press" style="left:790px">Metro Westbay</div>

<footer class="abs footer">
  <div class="foot-nav">Home<span class="sep">|</span>Speaking<span class="sep">|</span>Consulting<span class="sep">|</span>Training<span class="sep">|</span>Books<span class="sep">|</span>Resources<span class="sep">|</span>About<span class="sep">|</span>Contact<span class="sep">|</span>Testimonials</div>
  <div class="foot-rule"></div>
  <div class="foot-legal">Site Map<span style="margin:0 8px">|</span>Privacy Policy<span style="margin-left:20px">MorvaneLLC.com Copyright 2013. All rights reserved.</span></div>
  <div class="news-title">SUBSCRIBE TO OUR NEWSLETTER</div>
  <div class="field" style="left:784px;top:28px;width:164px;height:19px;line-height:17px;border-radius:2px">Email Address</div>
  <div class="abs" style="left:885px;top:32px;width:60px;height:12px;background:#555;color:#fff;font-size:7px;text-align:center;line-height:12px;border-radius:2px">SUBSCRIBE</div>
</footer>

</body>
</html>
```